LA's Newest HEMP Facial Oil and Body Oil Packaging Project

We need a packaging concept for a Hemp based facial oil and body oil. We need label design for the bottle and carton graphics. I am attaching a few reference photos. The target demographic is women between 17-35 year old. Products need to be able to stand out in crowded stores with clear calls to action.
1oz Dropper Bottle with Unit Carton - Hemp Facial Oil
4oz PET Bottle with Unit Carton - Hemp + Rose Facial Oil

```html
<!DOCTYPE html>
<html lang="en">
<head>
<meta charset="UTF-8">
<title>Hemp + Rose Facial Oil – Carton and Label</title>
<link rel="stylesheet" href="https://fonts.googleapis.com/css2?family=Montserrat:wght@700;800;900&family=Pinyon+Script&display=swap">
<style>
  :root {
    --bg: #e9e6e2;
    --panel: #fbfbfb;
    --panel-edge: #e2e2e2;
    --red: #e3464f;
    --red-deep: #d8333d;
    --rose-core: #ef4a52;
    --rose-mid: #f6a7ae;
    --rose-light: #fde3e6;
    --sprig: #8ea2d6;
    --ink: #3a3a3a;
    --white: #ffffff;
  }
  * { box-sizing: border-box; margin: 0; padding: 0; }
  html, body { width: 918px; height: 1200px; overflow: hidden; }
  body {
    background: var(--bg);
    font-family: "Montserrat", Arial, sans-serif;
    position: relative;
  }

  /* ---------- Carton front panel ---------- */
  .carton {
    position: absolute;
    left: 40px; top: 170px;
    width: 440px; height: 860px;
    background: linear-gradient(180deg, var(--white) 0%, var(--panel) 60%, #f1f1f1 100%);
    border: 1px solid var(--panel-edge);
    overflow: hidden;
  }
  .carton__title {
    position: absolute;
    top: 80px; left: 0; right: 0;
    text-align: center;
    color: var(--red);
    font-weight: 900;
    font-size: 86px;
    line-height: 0.98;
    letter-spacing: -1px;
  }
  .tagline {
    position: absolute;
    left: 36px; right: 36px;
    height: 30px;
    border: 1.5px solid var(--red);
    display: flex; align-items: center; justify-content: center;
  }
  .tagline span {
    font-family: "Pinyon Script", cursive;
    color: var(--ink);
    background: transparent;
    white-space: nowrap;
  }
  .carton .tagline { top: 488px; }
  .carton .tagline span { font-size: 46px; margin-top: -8px; }

  .rose-art {
    position: absolute;
    background:
      radial-gradient(circle at 42% 50%, var(--rose-core) 0%, var(--rose-mid) 22%, #f8c3c8 42%, var(--rose-light) 62%, rgba(253,227,230,0) 72%);
  }
  .sprig-art {
    position: absolute;
    background: radial-gradient(ellipse at 30% 50%, rgba(142,162,214,0.35) 0%, rgba(142,162,214,0) 70%);
  }
  .carton .rose-art { left: -40px; top: 560px; width: 380px; height: 300px; }
  .carton .sprig-art { left: 250px; top: 620px; width: 150px; height: 170px; }

  .with-note {
    position: absolute;
    text-align: right;
    color: var(--red-deep);
    font-weight: 700;
    line-height: 1.05;
    text-transform: uppercase;
  }
  .carton .with-note { right: 34px; top: 584px; font-size: 19px; }

  .size-tab {
    position: absolute;
    left: 50%;
    transform: translateX(-50%);
    background: var(--red);
    color: var(--white);
    font-weight: 700;
    text-align: center;
    border-radius: 999px 999px 0 0;
  }
  .carton .size-tab { bottom: 0; width: 130px; height: 62px; font-size: 28px; line-height: 70px; }

  /* ---------- Bottle label ---------- */
  .label {
    position: absolute;
    left: 520px; top: 390px;
    width: 360px; height: 420px;
    background: linear-gradient(180deg, var(--white) 0%, var(--panel) 70%, #f3f3f3 100%);
    border: 1px solid var(--panel-edge);
    overflow: hidden;
  }
  .label__title {
    position: absolute;
    top: 40px; left: 0; right: 0;
    text-align: center;
    color: var(--red);
    font-weight: 900;
    font-size: 37px;
    line-height: 1.08;
    letter-spacing: -0.5px;
  }
  .label .tagline { top: 150px; left: 70px; right: 70px; height: 20px; border-width: 1px; }
  .label .tagline span { font-size: 26px; margin-top: -4px; }
  .label .rose-art { left: 10px; top: 180px; width: 220px; height: 200px; }
  .label .sprig-art { left: 180px; top: 230px; width: 150px; height: 120px; }
  .label .with-note { right: 62px; top: 200px; font-size: 14px; }
  .label .size-tab { bottom: 0; width: 84px; height: 42px; font-size: 19px; line-height: 48px; }
</style>
</head>
<body>

  <section class="carton" aria-label="Carton front panel">
    <h1 class="carton__title">Hemp+<br>Rose<br>Facial<br>Oil</h1>
    <div class="tagline"><span>For all skin types</span></div>
    <div class="rose-art" role="img" aria-label="Illustration of a pink rose bloom"></div>
    <div class="sprig-art" role="img" aria-label="Illustration of fine blue flower sprigs"></div>
    <p class="with-note">With<br>Hemp Oil<br>&amp; Rose</p>
    <div class="size-tab">4oz</div>
  </section>

  <section class="label" aria-label="Bottle label">
    <h2 class="label__title">Hemp+Rose<br>Facial Oil</h2>
    <div class="tagline"><span>For all skin types</span></div>
    <div class="rose-art" role="img" aria-label="Illustration of a pink rose bloom"></div>
    <div class="sprig-art" role="img" aria-label="Illustration of fine blue flower sprigs"></div>
    <p class="with-note">With<br>Hemp Oil<br>&amp; Rose</p>
    <div class="size-tab">4oz</div>
  </section>

</body>
</html>
```